7:40 Steady Compass- A Handbook For Shaping Your Daily Conduct Each Morning

7:40 Steady Compass
A Handbook For Shaping Your Daily Conduct Each Morning

It will be a 6 X 9 guide that is meant for people to keep with them with pages to fill out. See supporting pics for overall pillars that are discussed and form basis of the solution.

I will need a spine and back cover as well.

My blog and content: www.morvenqlisk.com

Target Market(s)

Business professionals, senior emergency services people

Industry/Entity Type

Business Management

Font styles to use
Serif

Colors

Designer to choose colors to be used in the design.

Requirements
Must have
• Clean look, easily recognizable among other books. Front cover and back and spine. My picture on the back somewhere (corner maybe?!)
Nice to have
• Easily recognizeable
• NOTE: Graphic should read Today, Was I the Leader That I Would Want? I uploaded graphic that says ..."I Would've Wanted" which is incorrect.
Should not have
• Busy cover

```html
<!DOCTYPE html>
<html lang="en">
<head>
<meta charset="utf-8">
<title>7:40 Steady Compass — Front Cover</title>
<link rel="stylesheet" href="https://fonts.googleapis.com/css2?family=Tinos&display=swap">
<style>
  :root {
    --navy: #1f2939;
    --navy-band: #1d2636;
    --ivory: #ffffff;
    --stone-light: #e6dcc6;
    --stone-mid: #cbbd9f;
    --stone-dark: #a8997b;
  }
  * { margin: 0; padding: 0; box-sizing: border-box; }
  html, body { width: 795px; height: 1200px; overflow: hidden; background: var(--navy); }
  .cover {
    position: relative;
    width: 795px;
    height: 1200px;
    background: var(--navy);
    font-family: "Tinos", "Times New Roman", serif;
    color: var(--ivory);
    overflow: hidden;
  }
  .pillar {
    position: absolute;
    top: 0;
    width: 203px;
    height: 1006px;
  }
  .pillar--left { left: 0; }
  .pillar--right { right: 0; }
  .title-block {
    position: absolute;
    left: 0;
    width: 795px;
    text-align: center;
  }
  .title-number {
    top: 222px;
    font-size: 200px;
    line-height: 1;
    letter-spacing: 2px;
  }
  .title-words {
    top: 452px;
    font-size: 96px;
    line-height: 125px;
  }
  .title-rule {
    position: absolute;
    left: 260px;
    top: 703px;
    width: 276px;
    height: 7px;
    border-radius: 4px;
    background: var(--ivory);
  }
  .subtitle {
    top: 762px;
    font-size: 29px;
    line-height: 42px;
  }
  .author-band {
    position: absolute;
    left: 0;
    top: 1006px;
    width: 795px;
    height: 194px;
    background: var(--navy-band);
  }
  .author-name {
    position: absolute;
    left: 0;
    width: 795px;
    top: 1038px;
    text-align: center;
    font-size: 110px;
    line-height: 1;
    white-space: nowrap;
  }
</style>
</head>
<body>
<main class="cover">
  <svg class="pillar pillar--left" viewBox="0 0 203 1006" role="img" aria-label="Classical Ionic stone columns framing the left edge">
    <defs>
      <linearGradient id="stoneLeft" x1="0" x2="1" y1="0" y2="0">
        <stop offset="0" stop-color="var(--stone-dark)"/>
        <stop offset="0.45" stop-color="var(--stone-light)"/>
        <stop offset="1" stop-color="var(--stone-mid)"/>
      </linearGradient>
    </defs>
    <path d="M0 0 H203 V148 H148 V1006 H0 Z" fill="url(#stoneLeft)"/>
  </svg>

  <svg class="pillar pillar--right" viewBox="0 0 203 1006" role="img" aria-label="Classical Ionic stone columns framing the right edge">
    <defs>
      <linearGradient id="stoneRight" x1="0" x2="1" y1="0" y2="0">
        <stop offset="0" stop-color="var(--stone-mid)"/>
        <stop offset="0.55" stop-color="var(--stone-light)"/>
        <stop offset="1" stop-color="var(--stone-dark)"/>
      </linearGradient>
    </defs>
    <path d="M0 0 H203 V1006 H55 V148 H0 Z" fill="url(#stoneRight)"/>
  </svg>

  <h1>
    <span class="title-block title-number">7:40</span>
    <span class="title-block title-words">Steady<br>Compass</span>
  </h1>
  <div class="title-rule"></div>
  <p class="title-block subtitle">A Handbook For Shaping Your<br>Daily Conduct Each Morning</p>

  <div class="author-band"></div>
  <p class="author-name">Morven Q. Lisk</p>
</main>
</body>
</html>
```